Create look and feel for existing Web Page

Update Web Page

We have a website at http://www.usekivra.com/index-web.html. It is a single page html site, with a custom signup form. We also have a quill bay plugin at the bottom of the page. We'd like to redesign the look and feel of the entire site. We sell software to eye doctors. Also called optometrists, our software tool makes it easy for doctors to manage patients, bill, and document patient encounters. I have included our logos below.

We are looking for a new design preferably in HTML 5, CSS etc. The fields on the form on this page: http://www.usekivra.com/index-web.html

You can get screen shots of our software application at this site: http://staging.usekivra.com
username: test@samplevora.com
password: password

```html
<!DOCTYPE html>
<html lang="en">
<head>
<meta charset="utf-8">
<title>Ocuvane — Lease Practices</title>
<link href="https://fonts.googleapis.com/css2?family=Oswald:wght@300;400;500&family=Poppins:wght@300;400;500&display=swap" rel="stylesheet">
<style>
:root{
  --orange:#f7841a;
  --orange-dark:#ee6a08;
  --orange-soft:#fde3c8;
  --ink:#2a2a2a;
  --slate:#3f4452;
  --muted:#6b6b6b;
  --band:#efefef;
  --footer:#2b2b2b;
  --line:#d6d6d6;
  --white:#ffffff;
}
*{margin:0;padding:0;box-sizing:border-box}
html,body{width:1200px;height:4036px;overflow:hidden}
body{position:relative;background:var(--white);font-family:'Poppins',sans-serif;color:var(--ink)}
.abs{position:absolute}
.display{font-family:'Oswald',sans-serif;font-weight:500;letter-spacing:1px;color:var(--ink)}
.body-text{font-size:12px;line-height:23px;color:var(--muted)}

/* nav */
.site-nav{left:0;top:0;width:1200px;height:75px;background:var(--white);box-shadow:0 4px 14px rgba(0,0,0,.06);z-index:2}
.brand{font-family:'Poppins',sans-serif;font-weight:500;color:var(--orange);font-size:34px;letter-spacing:2px}
.site-nav .brand{left:150px;top:12px}
.nav-link{top:28px;font-size:13px;color:var(--ink)}
.nav-link.active::after{content:"";position:absolute;left:0;right:0;top:34px;height:3px;background:var(--orange)}
.btn-signup{left:953px;top:17px;width:97px;height:38px;background:var(--slate);color:#fff;font-size:13px;display:flex;align-items:center;justify-content:center;border-radius:2px}

/* hero */
.hero-title{left:150px;top:203px;font-size:44px;line-height:47px}
.hero-copy{left:150px;top:376px;width:415px}
.btn-orange{background:var(--orange);color:#fff;font-size:13px;display:flex;align-items:center;justify-content:center;border-radius:2px}
.hero-cta{left:150px;top:501px;width:235px;height:38px}
.art-fill{border-radius:50%;background:radial-gradient(circle at 50% 55%,#fcd9b4,var(--orange-soft))}

/* dashboard band */
.band{left:0;top:688px;width:1200px;height:606px;background:var(--band)}
.dash{left:149px;top:772px;width:901px;height:427px;background:#f4f4f4;border-radius:6px;overflow:hidden;box-shadow:0 2px 8px rgba(0,0,0,.08)}
.dash-side{left:0;top:0;width:157px;height:427px;background:linear-gradient(#3d4150,#5b5f6b 55%,#e6e6e6)}
.dash-side .brand{font-size:14px;left:10px;top:6px}
.dash-menu{left:0;width:148px;height:20px;font-size:8px;color:#fff;padding-left:30px;line-height:20px}
.dash-main{left:157px;top:0;width:744px;height:395px;background:#fff}
.stat{top:246px;width:228px;height:116px;background:linear-gradient(#5a5f6d,#8a8e99);border-radius:3px;color:#fff;padding:10px}
.stat h4{font-weight:400;font-size:12px}
.stat small{font-size:6px;display:block;opacity:.8}
.stat b{font-weight:300;font-size:22px;display:block;margin-top:12px}
.stat .tabs{position:absolute;bottom:6px;left:10px;right:10px;display:flex;justify-content:space-around;font-size:6px}

/* features */
.eyebrow{font-family:'Oswald',sans-serif;font-weight:300;font-size:18px;letter-spacing:4px;color:var(--ink)}
.feat-title{left:152px;top:1478px;font-size:42px;line-height:47px}
.feat-copy{left:150px;top:1650px;width:330px}
.arrow-btn{width:66px;height:66px;border:2px solid var(--ink);border-radius:50%;display:flex;align-items:center;justify-content:center}
.feature-card{left:588px;width:462px;height:137px;background:#fff;box-shadow:0 4px 16px rgba(0,0,0,.09);display:flex;align-items:center}
.feature-card .label{width:160px;text-align:center;font-family:'Oswald',sans-serif;font-weight:400;font-size:21px;color:var(--ink)}
.feature-card .label svg{display:block;margin:0 auto 8px}
.feature-card .divider{width:1px;height:62px;background:var(--line)}
.feature-card p{padding-left:26px;width:260px;font-size:11px;line-height:23px;color:var(--muted)}
.ghost-card{left:1081px;width:160px;height:137px;background:#fff;box-shadow:0 4px 16px rgba(0,0,0,.05);text-align:center;padding-top:82px;font-family:'Oswald',sans-serif;font-weight:300;font-size:21px;color:#c8c8c8}
.ghost-card span{display:block;position:relative;left:-30px}

/* pricing */
.pricing-title{left:0;width:1200px;top:2178px;text-align:center;font-size:42px}
.plan{background:#fff;box-shadow:0 8px 24px rgba(0,0,0,.08);text-align:center}
.plan-head{position:relative;height:82px;background:#f1f1f1;font-family:'Oswald',sans-serif;font-weight:300;font-size:24px;color:var(--orange);padding-top:28px;clip-path:polygon(0 0,100% 0,100% 75%,50% 100%,0 75%)}
.plan p{font-size:11px;line-height:22px;color:var(--muted);padding:0 45px}
.price{font-family:'Oswald',sans-serif;color:var(--orange);font-size:46px;margin-top:24px}
.price sub{font-size:14px;vertical-align:baseline}
.per{font-family:'Oswald',sans-serif;font-weight:300;font-size:17px;color:var(--ink)}
.plan.featured{background:linear-gradient(#f89a3d,var(--orange-dark));color:#fff}
.plan.featured .plan-head{background:#f9a152;color:#fff;height:90px}
.plan.featured p,.plan.featured .price,.plan.featured .per{color:#fff}
.dot{top:2751px;width:8px;height:8px;border-radius:50%;background:var(--ink)}

/* cta */
.cta-title{left:696px;top:2972px;font-size:44px;line-height:47px}
.btn-slate{left:696px;top:3167px;width:136px;height:38px;background:var(--slate);color:#fff;font-size:12px;display:flex;align-items:center;justify-content:center;border-radius:2px}

/* footer */
.site-footer{left:0;top:3404px;width:1200px;height:632px;background:var(--footer)}
.site-footer .eyebrow{color:#ddd}
.waitlist-title{color:#fff}
.field{height:36px;border:1px solid #9a9a9a;border-radius:18px;color:#bdbdbd;font-size:12px;padding-left:18px;line-height:34px}
.social{width:28px;height:28px;border-radius:50%}
.copyright{color:#ddd;font-size:12px}
</style>
</head>
<body>

<header class="abs site-nav">
  <div class="abs brand">ocuvane</div>
  <a class="abs nav-link active" style="left:710px">Home</a>
  <a class="abs nav-link" style="left:774px">Products</a>
  <a class="abs nav-link" style="left:855px">Pricing</a>
  <a class="abs btn-signup">Sign Up</a>
</header>

<!-- hero -->
<svg class="abs" style="left:700px;top:300px" width="500" height="400" viewBox="0 0 500 400" fill="none" stroke="#dcdcdc">
  <circle cx="480" cy="340" r="260"/>
  <path d="M400 390 C430 320 470 300 500 300"/>
</svg>
<h1 class="abs display hero-title">Lease Practices: Choose<br>How You Spend Your<br>Time</h1>
<p class="abs body-text hero-copy">Ocuvane is your office operating system. Automate your painful tasks, keep track of your books, and live a little. Start with a FREE charting tool and add more prod</p>
<a class="abs btn-orange hero-cta">Get The Charting Tool For Free</a>
<div class="abs art-fill" style="left:674px;top:152px;width:448px;height:448px" role="img" aria-label="Illustration of a person working on a laptop at a desk, with location and globe icons"></div>

<!-- dashboard preview -->
<section class="abs band"></section>
<div class="abs dash">
  <div class="abs dash-side">
    <div class="abs brand">ocuvane</div>
    <div class="abs" style="left:0;width:157px;top:50px;text-align:center;color:#fff;font-size:8px">John Doe<br><span style="font-size:6px;opacity:.7">test@samplevora.com</span></div>
    <div class="abs" style="left:56px;top:92px;width:44px;height:44px;border-radius:50%;background:#8e929c;border:2px solid #fff" role="img" aria-label="User profile photo"></div>
    <div class="abs dash-menu" style="top:137px;background:#1e90e6;border-radius:0 10px 10px 0">Dashboard</div>
    <div class="abs dash-menu" style="top:160px">Calendar</div>
    <div class="abs dash-menu" style="top:183px">Search</div>
    <div class="abs dash-menu" style="top:206px">Settings</div>
    <div class="abs dash-menu" style="top:228px">Patient Engagement</div>
    <div class="abs dash-menu" style="top:250px">Logout</div>
  </div>
  <div class="abs dash-main">
    <div class="abs" style="left:10px;top:10px;font-size:11px;font-weight:500">John's LLC <span style="font-size:6px;font-weight:300">(Active)</span></div>
    <div class="abs" style="left:0;top:36px;width:744px;height:2px;background:#e2e2e2"></div>
    <div class="abs" style="left:14px;top:50px;font-size:9px">Total Patient's Chart : 2<br><span style="font-size:6px;color:#999">Daily Appointments</span></div>
    <div class="abs" style="left:606px;top:58px;font-size:6px;color:#666">16 MAR &nbsp; 17 MAR &nbsp; <span style="color:#bbb">18 MAR</span></div>
    <svg class="abs" style="left:14px;top:90px" width="710" height="120" viewBox="0 0 710 120">
      <line x1="4" y1="114" x2="706" y2="114" stroke="#ccc"/>
      <line x1="4" y1="0" x2="4" y2="114" stroke="#eee"/>
      <path d="M310 114 C325 114 325 0 335 0 C345 0 345 114 360 114Z" fill="#2e8fe0"/>
      <path d="M318 114 C330 114 330 54 335 54 C340 54 340 114 352 114Z" fill="#575b67"/>
      <path d="M485 114 C500 114 500 56 508 56 C516 56 516 114 531 114Z" fill="#575b67"/>
    </svg>
    <div class="abs stat" style="left:10px"><h4>Sales Revenue</h4><small>Lifetime sum of your sales</small><b>0</b><div class="tabs"><span>1DAY</span><span>1WEEK</span><span>1MONTH</span></div></div>
    <div class="abs stat" style="left:258px"><h4>Cash Revenue</h4><small>Lifetime sum of your sales</small><b>0</b><div class="tabs"><span>1DAY</span><span>1WEEK</span><span>1MONTH</span></div></div>
    <div class="abs stat" style="left:506px"><h4>Credit Card Revenue</h4><small>Lifetime sum of your sales</small><b>0</b><div class="tabs"><span>1DAY</span><span>1WEEK</span><span>1MONTH</span></div></div>
  </div>
  <div class="abs" style="right:10px;bottom:12px;font-size:6px;color:#fff">© Ocuvane 2019. All rights reserved</div>
</div>

<!-- features -->
<div class="abs eyebrow" style="left:152px;top:1440px">JOIN THE COOL CLUB</div>
<h2 class="abs display feat-title">AI To Automate<br>Optometry Office<br>Tasks</h2>
<p class="abs body-text feat-copy">Ocuvane uses AI, automation, robots, and other cool technology to streamline office work so you can do things you love</p>
<div class="abs arrow-btn" style="left:150px;top:1766px"><svg width="16" height="16" viewBox="0 0 16 16" fill="none" stroke="#2a2a2a" stroke-width="2.5"><path d="M10 2 4 8l6 6"/></svg></div>
<div class="abs arrow-btn" style="left:228px;top:1766px"><svg width="16" height="16" viewBox="0 0 16 16" fill="none" stroke="#2a2a2a" stroke-width="2.5"><path d="M6 2l6 6-6 6"/></svg></div>

<div class="abs feature-card" style="top:1443px">
  <div class="label"><svg width="40" height="40" viewBox="0 0 40 40" fill="none" stroke="#f7841a" stroke-width="1.5"><rect x="3" y="7" width="30" height="26" rx="2"/><path d="M3 14h30M10 3v8M26 3v8"/><circle cx="31" cy="31" r="6" fill="#fff"/><path d="M28 31l2 2 4-4"/></svg>Schedule</div>
  <div class="divider"></div>
  <p>Meet your patients where they are, 24 hours 7 days a week with the online scheduler.</p>
</div>
<div class="abs feature-card" style="top:1592px">
  <div class="label"><svg width="40" height="40" viewBox="0 0 40 40" fill="none" stroke="#f7841a" stroke-width="1.5"><circle cx="15" cy="15" r="8"/><circle cx="15" cy="15" r="3"/><circle cx="28" cy="28" r="6"/><circle cx="28" cy="28" r="2"/></svg>Intake</div>
  <div class="divider"></div>
  <p>Never print out another paper form. Your patients are now able to fill out and sign forms online.</p>
</div>
<div class="abs feature-card" style="top:1742px">
  <div class="label"><svg width="40" height="40" viewBox="0 0 40 40" fill="none" stroke="#f7841a" stroke-width="1.5"><path d="M6 36h30M9 36V26h5v10M18 36V20h5v10M27 36V14h5v22M6 22l10-8 6 4 12-12M30 6h4v4"/></svg>Chart</div>
  <div class="divider"></div>
  <p>Start charting all patient findings for FREE. With features like auto population it flies on your mobile phone.</p>
</div>
<div class="abs ghost-card" style="top:1443px"><span>Bill</span></div>
<div class="abs ghost-card" style="top:1592px"><span>Eligible</span></div>
<div class="abs ghost-card" style="top:1742px"><span>Review</span></div>

<svg class="abs" style="left:0;top:1920px" width="1200" height="210" viewBox="0 0 1200 210" fill="none" stroke="#c9c9c9" stroke-width="1.5">
  <path d="M0 200 C200 80 420 60 620 120 C820 180 1000 140 1200 10"/>
  <path d="M0 180 C250 110 450 100 640 140 C860 185 1040 150 1200 40"/>
</svg>

<!-- pricing -->
<h2 class="abs display pricing-title">Pricing</h2>
<div class="abs plan" style="left:174px;top:2316px;width:273px;height:340px">
  <div class="plan-head">Free</div>
  <p style="margin-top:40px">Chart patient findings for FREE. Unlimited users, doctors, and location.</p>
  <div class="price">$00/<sub>mo</sub></div>
  <div class="per">No strings attached</div>
</div>
<div class="abs plan" style="left:754px;top:2316px;width:272px;height:340px">
  <div class="plan-head">Pick 2 Add On</div>
  <p style="margin-top:40px">Choose any two features between schedule, intake, bill, eligible, and/or review.</p>
  <div class="price">$189/<sub>mo</sub></div>
  <div class="per">per location</div>
</div>
<div class="abs plan featured" style="left:447px;top:2294px;width:307px;height:386px">
  <div class="plan-head">Pick 1 Add On</div>
  <p style="margin-top:48px">Choose between schedule, intake, bill, eligible, or review.</p>
  <div class="price">$99/<sub>mo</sub></div>
  <div class="per">per location</div>
</div>
<div class="abs dot" style="left:532px"></div>
<div class="abs dot" style="left:559px;background:#fff;border:2px solid var(--ink);width:12px;height:12px;top:2749px"></div>
<div class="abs dot" style="left:586px"></div>
<div class="abs dot" style="left:610px"></div>
<div class="abs dot" style="left:634px"></div>
<div class="abs dot" style="left:660px"></div>

<!-- cta -->
<svg class="abs" style="left:900px;top:2900px" width="300" height="500" viewBox="0 0 300 500" fill="none" stroke="#dcdcdc"><circle cx="300" cy="250" r="240"/></svg>
<div class="abs art-fill" style="left:103px;top:2863px;width:448px;height:448px" role="img" aria-label="Illustration of three smiling office team members surrounded by mail, globe, chat and location icons"></div>
<h2 class="abs display cta-title">Now Spend Time<br>Outside The<br>Office!</h2>
<a class="abs btn-slate">Join The Club</a>

<!-- footer / waitlist -->
<footer class="abs site-footer">
  <div class="abs eyebrow" style="left:150px;top:112px">GET ON THE WAITLIST</div>
  <h2 class="abs display waitlist-title" style="left:150px;top:148px;font-size:42px;line-height:47px">Get Started With A Free<br>Charting Tool</h2>
  <div class="abs field" style="left:150px;top:307px;width:245px">Full Name</div>
  <div class="abs field" style="left:403px;top:307px;width:244px">Email</div>
  <div class="abs field" style="left:150px;top:361px;width:245px">Cell Phone</div>
  <div class="abs field" style="left:403px;top:361px;width:244px">Office Name</div>
  <div class="abs field" style="left:150px;top:416px;width:497px">NPI</div>
  <a class="abs btn-orange" style="left:150px;top:482px;width:497px;height:36px">Get The Free Charting Tool</a>
  <div class="abs brand" style="right:152px;top:352px;font-size:40px">ocuvane</div>
  <div class="abs social" style="left:890px;top:435px;background:#c13584"></div>
  <div class="abs social" style="left:934px;top:435px;background:#0a66c2"></div>
  <div class="abs social" style="left:978px;top:435px;background:#3b5998"></div>
  <div class="abs social" style="left:1022px;top:435px;background:#1da1f2"></div>
  <div class="abs copyright" style="right:152px;top:503px">Copyright © 2020, ocuvane, all right reserved</div>
</footer>

</body>
</html>
```